Harwick Legal

To update and modernize current business card appearance. Marta's business is based in Melbourne with 4 other lawyers in the firm. Marta travels to the Pilbara in Western Australia approximately 1 week a month as part of the firms legal work. She consults with clients in Newman, Tom Price and Port Hedland. The lawyers work mostly from a home office, apart from court appearances. They have a virtual office in Melbourne city, and use facilities in 3 or 4 other locations around Melbourne. It is important the client's think this is a conventional law firm with a permanent office. Our business structure is a difficult concept for them to grasp. The business has been operational for 3 years, growing from 1 lawyer to 4 lawyers during that time. Our website is www.Harwicklegal.example.au and is currently being upgraded as we are not happy with its content. The logo is currently orange and dark grey but the orange is a difficult colour to reproduce and often turns out "poo" brown when documents are printed. We need clients to know we are user friendly and caring - and not head up our rears ends as some lawyers appear to be.
Updates

Thank you for the feedback so far. 1. Some of the designs have too much black (We prefer darker grey & not too much.) 2. Happy for designers to play around with different colours & logo design. What we're after is a modern look and business card that people say "wow" when they pick it up.

Industry/Entity Type

Business

```html
<!DOCTYPE html>
<html lang="en">
<head>
<meta charset="utf-8">
<title>Harwick Legal – Business Card</title>
<link rel="stylesheet" href="https://fonts.googleapis.com/css2?family=Questrial&display=swap">
<style>
  :root {
    --page-bg: #ecebe8;
    --card-front-top: #d3dde4;
    --card-front-bottom: #b9c7d1;
    --card-back-deep: #1f4a63;
    --card-back-light: #5d8fa6;
    --accent-red: #e0262b;
    --ink-white: #ffffff;
    --ink-grey: #3a3d40;
    --icon-grey: #f4f6f8;
  }
  * { box-sizing: border-box; margin: 0; padding: 0; }
  html, body {
    width: 1200px; height: 1000px; overflow: hidden;
    background: var(--page-bg);
    font-family: "Questrial", "Century Gothic", sans-serif;
  }
  .canvas {
    position: relative; width: 1200px; height: 1000px;
  }
  .card {
    position: absolute; top: 345px;
    width: 540px; height: 309px;
    border-radius: 4px;
    box-shadow: 0 10px 28px rgba(0,0,0,0.18);
    overflow: hidden;
  }
  /* Front: contact side */
  .card-front {
    left: 40px;
    background: linear-gradient(160deg, var(--card-front-top), var(--card-front-bottom));
  }
  .holder-name {
    position: absolute; left: 34px; top: 26px;
    font-size: 30px; color: var(--ink-white);
    letter-spacing: 0.5px;
  }
  .credentials {
    position: absolute; left: 70px; top: 70px;
    display: flex; flex-direction: column; gap: 5px; align-items: flex-start;
  }
  .pill {
    background: var(--ink-white);
    color: var(--accent-red);
    border-radius: 7px;
    padding: 2px 10px;
    font-size: 13px; font-weight: 700;
    line-height: 17px;
  }
  .contact-list {
    position: absolute; left: 34px; top: 132px;
    list-style: none;
    display: flex; flex-direction: column; gap: 7px;
  }
  .contact-item { display: flex; align-items: center; gap: 12px; }
  .contact-item svg { width: 18px; height: 18px; flex: none; }
  .service-area {
    position: absolute; left: 34px; bottom: 26px;
    font-size: 21px; color: var(--ink-white);
  }
  .front-brand {
    position: absolute; right: 34px; top: 176px;
    display: flex; align-items: center; gap: 8px;
    font-size: 19px; color: var(--ink-grey);
    letter-spacing: 1px;
  }
  .brand-dot {
    width: 14px; height: 14px; border-radius: 50%;
    background: var(--accent-red);
  }
  /* Back: brand side */
  .card-back {
    left: 620px;
    background: radial-gradient(ellipse at 45% 35%, var(--card-back-light), var(--card-back-deep) 85%);
  }
  .back-brand {
    position: absolute; left: 0; right: 0; top: 190px;
    display: flex; justify-content: center; align-items: center; gap: 14px;
    font-size: 40px; color: var(--ink-grey);
    letter-spacing: 3px;
  }
  .back-brand .brand-dot { width: 24px; height: 24px; }
</style>
</head>
<body>
<main class="canvas">

  <section class="card card-front" aria-label="Business card front">
    <h1 class="holder-name">J. Marta Quinlan</h1>
    <div class="credentials">
      <span class="pill">LLB (Hons) - Accredited Mediator</span>
      <span class="pill">Principal Solicitor</span>
    </div>
    <ul class="contact-list">
      <li class="contact-item">
        <svg viewBox="0 0 18 18" aria-hidden="true"><rect x="5" y="1.5" width="8" height="15" rx="1.5" fill="none" stroke="var(--icon-grey)" stroke-width="1.5"/><line x1="8" y1="14" x2="10" y2="14" stroke="var(--icon-grey)" stroke-width="1.5"/></svg>
        <span class="pill">0400 118 274</span>
      </li>
      <li class="contact-item">
        <svg viewBox="0 0 18 18" aria-hidden="true"><path d="M4 2 L7 2 L8 6 L6 7.5 C7 10 8 11 10.5 12 L12 10 L16 11 L16 14 C16 15 15 16 14 16 C8 15 3 10 2 4 C2 3 3 2 4 2 Z" fill="var(--icon-grey)"/></svg>
        <span class="pill">1300 HARWICK (427 942)</span>
      </li>
      <li class="contact-item">
        <svg viewBox="0 0 18 18" aria-hidden="true"><circle cx="9" cy="9" r="7" fill="none" stroke="var(--icon-grey)" stroke-width="1.5"/><ellipse cx="9" cy="9" rx="3" ry="7" fill="none" stroke="var(--icon-grey)" stroke-width="1.2"/><line x1="2" y1="9" x2="16" y2="9" stroke="var(--icon-grey)" stroke-width="1.2"/></svg>
        <span class="pill">marta.quinlan@harwicklegal.example.au</span>
      </li>
    </ul>
    <div class="front-brand"><span class="brand-dot"></span>HARWICK LEGAL</div>
    <p class="service-area">Melbourne Eastern And Bayside Suburbs</p>
  </section>

  <section class="card card-back" aria-label="Business card back">
    <div class="back-brand"><span class="brand-dot"></span>HARWICK LEGAL</div>
  </section>

</main>
</body>
</html>
```